Outdoor banner - allegorical car (float) on Gay Pride

We need a graphics for advertising banner promoting web project www.spektrovia.com
Approximate size 120x40inch (3x1meters) - Therefore, it is required vector graphics, any embedded bitmaps in high resolution.

We launching new social network and city guide application for Prague visitors.
Keywords for poster are: city, Prague, traveling, rainbow, party, colors, holiday,..
It must contain the dominant text "SPEKTROVIA.COM".
Banner will be placed on an float (allegorical car) in the parade Prague Colour Parade 2014. And this banner will be the dominant car graphics.

- modern party look
- it should be understood that it is the queer(gay) web :)
- appropriate use of rainbow colors( or elements) in the graphics
- is possible to use silhouette of Prague

update:
- preferred is a vector graphics (vector elements)
- with regard to the size of the banner is not suitable the one big bitmap photo
- banner will be horizontal
Updates

update: - preferred is a vector graphics (vector elements) - with regard to the size of the banner is not suitable the one big bitmap photo

Target Market(s)

Prague visitors ..looking for entertainment., services..

Industry/Entity Type

Advertising

Requirements
Must have
• dominant text "SPEKTROVIA.COM"
rainbow colors( or elements) in the graphics
vector graphics for large format printing

```html
<!DOCTYPE html>
<html lang="en">
<head>
<meta charset="utf-8">
<title>Spektrovia – Outdoor Parade Banner</title>
<link rel="stylesheet" href="https://fonts.googleapis.com/css2?family=Bebas+Neue&display=swap">
<style>
  :root {
    --ink: #050308;
    --night: #140a24;
    --violet: #5a2f8f;
    --lilac: #8a6fd8;
    --magenta: #c0207a;
    --laser-green: #3fbf7a;
    --white: #ffffff;
    --red: #e4202a;
    --orange: #f7931e;
    --yellow: #ffe100;
    --green: #2bb34a;
    --blue: #1f6fd1;
    --purple: #7a2ea0;
  }
  html, body {
    margin: 0;
    padding: 0;
    width: 1200px;
    height: 400px;
    overflow: hidden;
    background: var(--ink);
  }
  .banner {
    position: relative;
    width: 1200px;
    height: 400px;
    overflow: hidden;
    background: var(--ink);
    font-family: "Bebas Neue", "Oswald", sans-serif;
  }
  .party-scene {
    position: absolute;
    left: 0;
    top: 34px;
    width: 1200px;
    height: 326px;
    background:
      radial-gradient(ellipse 420px 150px at 50% 10%, rgba(138,111,216,0.85), transparent 70%),
      radial-gradient(ellipse 300px 110px at 25% 30%, rgba(90,47,143,0.7), transparent 70%),
      radial-gradient(ellipse 300px 110px at 78% 30%, rgba(90,47,143,0.7), transparent 70%),
      radial-gradient(ellipse 260px 90px at 20% 85%, rgba(192,32,122,0.45), transparent 70%),
      radial-gradient(ellipse 220px 80px at 85% 80%, rgba(63,191,122,0.35), transparent 70%),
      linear-gradient(180deg, var(--violet) 0%, var(--night) 55%, var(--ink) 100%);
  }
  .rainbow-band {
    position: absolute;
    left: 0;
    width: 1200px;
    height: 40px;
    background: linear-gradient(180deg,
      var(--ink) 0%, var(--ink) 14%,
      var(--purple) 14%, var(--purple) 28%,
      var(--blue) 28%, var(--blue) 42%,
      var(--green) 42%, var(--green) 56%,
      var(--yellow) 56%, var(--yellow) 70%,
      var(--orange) 70%, var(--orange) 84%,
      var(--red) 84%, var(--red) 100%);
  }
  .rainbow-band--top { top: 0; transform: scaleY(-1); }
  .rainbow-band--bottom { bottom: 0; }
  .headline {
    position: absolute;
    left: 0;
    top: 0;
    width: 1200px;
    height: 400px;
  }
  .headline-text {
    font-family: "Bebas Neue", "Oswald", sans-serif;
    font-size: 200px;
    fill: var(--white);
  }
  .tagline {
    position: absolute;
    left: 0;
    top: 268px;
    width: 1200px;
    margin: 0;
    text-align: center;
    color: var(--white);
    font-size: 52px;
    line-height: 1;
    letter-spacing: 1px;
  }
</style>
</head>
<body>
  <div class="banner">
    <div class="party-scene" role="img" aria-label="Night party scene with purple laser lights over a Prague skyline and a dancing crowd"></div>
    <div class="rainbow-band rainbow-band--top"></div>
    <div class="rainbow-band rainbow-band--bottom"></div>

    <svg class="headline" viewBox="0 0 1200 400" xmlns="http://www.w3.org/2000/svg">
      <text class="headline-text" x="600" y="238" text-anchor="middle"
            textLength="1020" lengthAdjust="spacingAndGlyphs">SPEKTROVIA.COM</text>
    </svg>

    <p class="tagline">ENJOY THE BEST OF PRAGUE</p>
  </div>
</body>
</html>
```